Этикетка для флакона моющего средства
Задание на дизайн
Размер
82 мм × 180 мм
Опишите свою организацию или продукт и целевую аудиторию
Этикетка для серии специальных моющих средств, готовых к применению.
Например пятновыводитель для ковров, удалитель следов скотча и фломастера, очиститель ржавчины.
Наши моющие средства применяют как профессиональные уборщики (клинеры), так и «продвинутые домохозяйки».
Основная идея этикетки — современный минималистичный дизайн, отсутствие лишнего информационного шума, на домашней полке и в руках профессионала должно выглядеть как профессиональное средство, где упор на содержимое, на удобство пользования, а не на кричащую этикетку. Обратите внимание на фото, как будет выглядеть сам флакон, на который необходимо сделать этикетку, флакон белого цвета.
Этикетка содержит 3 блока — 1) название и лицевая часть 2) служебная часть (данные производителя, состав, штрих код и т. д. 3) информационная часть по применению — инструкция, перечень удаляемых загрязнений, подходящие поверхности для удаления
Текстовое содержание этикетки — в прилагаемом файле.
Обратите внимание 1) На лицевой части указывается величина pH продукта, при этом цвет этой надписи (или части оформления фронта этикетки) должен быть зеленой в случае кислотного, красной — щелочного, фиолетовый -нейтрального состава, но этот цвет не должен доминировать. 2) Информационную часть хотелось бы выполнить в виде пиктограмм и/или инфографики, там получится 3 группы информационной: «удаляет», «подходит», «применение» . Желательно чтобы в информационной части текста вообще не было, максимум пояснения к рисункам — пиктограммам.
Примеры пиктограмм и этикеток даны в приложении, но это не образцы для копирования, просто направление для творчества Вашего)
Приложите логотипы или другие материалы
Это флакон для которого необходимо разработать этикетку
Это наш логотип
Минималистичный дизайн
лаконичные пиктограммы
Это полный текст этикетки
приятный минимализм, но в нашем случае эко-тему не эксплуатируем
Это наш флакон
Комментарии и пожелания для дизайнеров
Эко тему не эксплуатируем, это для другой линейки, основной показатель здесь - эффективность.
Чтобы не было большого разноцветия в этикетке - цвета полосок в логотипе можно делать того же цвета, что и задан pH средства - то есть зеленым, фиолетовым или оранжевым.

```html
<!DOCTYPE html>
<html lang="ru">
<head>
<meta charset="utf-8">
<title>Универсал растворитель — этикетка</title>
<link href="https://fonts.googleapis.com/css2?family=Manrope:wght@300;400;600;700;800&display=swap" rel="stylesheet">
<style>
  :root {
    --bg: #b1b1b1;
    --label: #ffffff;
    --ink: #1d1d1f;
    --line: #2a2a2a;
    --ph-neutral: #a57db8;
    --accent: #9a6bb0;
  }
  * { box-sizing: border-box; margin: 0; padding: 0; }
  html, body { width: 1200px; height: 966px; overflow: hidden; }
  body {
    background: var(--bg);
    font-family: "Manrope", Arial, sans-serif;
    color: var(--ink);
    position: relative;
  }
  .label {
    position: absolute;
    left: 250px; top: 135px;
    width: 720px; height: 696px;
    background: var(--label);
    border-radius: 10px;
  }
  .front {
    position: absolute;
    left: 50px; top: 50px;
    width: 551px; height: 595px;
    border: 2px solid var(--line);
    display: grid;
    grid-template-rows: 143px 166px 143px 1fr;
  }
  .row { border-bottom: 2px solid var(--line); position: relative; display: flex; align-items: center; }
  .row:last-child { border-bottom: none; }
  .brand-row { display: grid; grid-template-columns: 161px 1fr; }
  .brand-cell {
    border-right: 2px solid var(--line);
    display: flex; align-items: center; justify-content: center; gap: 8px;
  }
  .brand-dot { width: 12px; height: 12px; border-radius: 50%; background: var(--accent); }
  .brand-name { font-weight: 800; font-size: 22px; color: var(--ink); letter-spacing: 1px; }
  .product-name {
    padding-left: 48px;
    font-weight: 800; font-size: 36px; line-height: 1.2;
    text-transform: uppercase;
  }
  .subtitle {
    padding-left: 48px;
    font-weight: 700; font-size: 28px; line-height: 1.3;
  }
  .row-icon { position: absolute; right: 38px; top: 50%; transform: translateY(-50%); }
  .ph-row { align-items: stretch; }
  .ph-text { padding-left: 48px; align-self: center; font-weight: 700; font-size: 28px; line-height: 1.3; flex: 1; }
  .ph-value {
    width: 226px;
    background: var(--ph-neutral);
    color: #fff;
    font-weight: 300; font-size: 72px;
    display: flex; align-items: center; justify-content: center;
  }
  .usage {
    position: absolute;
    left: 625px; top: 50px;
    width: 80px;
  }
  .usage-title { font-weight: 800; font-size: 11px; margin-bottom: 4px; }
  .usage-item { margin-bottom: 22px; }
  .usage-caption { font-weight: 700; font-size: 10px; margin-bottom: 6px; }
  .usage-icon { width: 40px; height: 40px; border: 2px solid var(--accent); border-radius: 4px; position: relative; }
  .usage-icon::after {
    content: ""; position: absolute; left: 13px; top: 13px;
    width: 10px; height: 10px; border-radius: 50%; background: var(--accent);
  }
</style>
</head>
<body>
  <div class="label">
    <div class="front">
      <div class="row brand-row">
        <div class="brand-cell"><span class="brand-dot"></span><span class="brand-name">ТЕКСО</span></div>
        <div></div>
      </div>
      <div class="row">
        <div class="product-name">Универсал<br>растворитель</div>
        <svg class="row-icon" width="34" height="52" viewBox="0 0 34 52" fill="none" stroke="var(--accent)" stroke-width="2.5">
          <rect x="8" y="2" width="18" height="7" rx="2"/>
          <rect x="3" y="9" width="28" height="41" rx="5"/>
          <text x="17" y="36" text-anchor="middle" font-family="Manrope, sans-serif" font-size="16" font-weight="700" fill="var(--accent)" stroke="none">S</text>
        </svg>
      </div>
      <div class="row">
        <div class="subtitle">Профессиональная<br>химия</div>
        <svg class="row-icon" width="42" height="50" viewBox="0 0 42 50" fill="none" stroke="var(--accent)" stroke-width="2.5" stroke-linejoin="round">
          <path d="M15 3h12M17 3v16L4 45h34L25 19V3"/>
          <circle cx="17" cy="36" r="2.5" fill="var(--accent)" stroke="none"/>
          <circle cx="25" cy="31" r="2" fill="var(--accent)" stroke="none"/>
        </svg>
      </div>
      <div class="row ph-row">
        <div class="ph-text">Нейтральный<br>ph</div>
        <div class="ph-value">7.5</div>
      </div>
    </div>
    <div class="usage">
      <div class="usage-title">Удаляет</div>
      <div class="usage-item"><div class="usage-caption">Спирт</div><div class="usage-icon"></div></div>
      <div class="usage-item"><div class="usage-caption">Лак</div><div class="usage-icon"></div></div>
      <div class="usage-item"><div class="usage-caption">Пятна</div><div class="usage-icon"></div></div>
      <div class="usage-item"><div class="usage-caption">Фломастер</div><div class="usage-icon"></div></div>
      <div class="usage-item"><div class="usage-caption">Тонер</div><div class="usage-icon"></div></div>
    </div>
  </div>
</body>
</html>
```